依頼詳細
★★★ランディングページに必ず入れて欲しい文言です★★★
----------------------------------
■キャッチ
ページ制作5ページ+問い合わせフォーム+初期費用
通常価格:149,100円(税込)
6/28までの限定キャンペーン!!先着10名まで!!

キャンペーン価格63,000円(税込み)
※初期費用は、ドメイン取得代行・レンタルサーバ取得代行を含みます。
※ページ制作は5ページまでとなります。
※ドメイン代<年額:850円~>、レンタルサーバ代<年額4,725円~>は別途お客様にてご負担頂きます。
※ホームページに掲載する画像を撮影することも可能です(但し、別途費用が発生します)

■3つのポイント
1.SEOで上位表示を行います
2.PC・スマートフォンに最適化されたページを提供します
3.納品後のサポート6ヶ月無料サービス付き

■問い合わせフォーム

サイトURL
karunetox.co.jp
ページ数
1ページ
希望イメージ
シンプル 複雑
単色 カラフル
暗い 明るい
日常 高級
遊び心 厳粛
未来的 伝統的
女性的 男性的
希望する色
青、オレンジ、白
納品ファイル
• 高解像度JPG (.jpg)
• イラストレーター形式 (.ai)
• フォトショップ形式 (.psd)
• PNG形式 (.png)
補足説明
■ 重視する点/検討基準
・予算
・ランディングページ(LP)を作成をした経験
・過去のランディングページ(LP)作成実績を公開して頂けること
・LPOを意識したデザインをして頂けること
・ランディングページ(LP)をリスティングで利用した経験

■ 利用用途
Lumora Clickpostのリンク先として使用します。

■ 納品形式
各レイヤー毎に分かれたpsdファイルで納品をお願いします。

```html
<!DOCTYPE html>
<html lang="ja">
<head>
<meta charset="utf-8">
<title>karunetox キャンペーン</title>
<link href="https://fonts.googleapis.com/css2?family=Noto+Sans+JP:wght@400;700;900&display=swap" rel="stylesheet">
<style>
:root{
  --bg:#d9d9d9;
  --panel:#ffffff;
  --blue:#1d8fd6;
  --blue-dark:#0b5fa5;
  --blue-light:#e3f1fb;
  --orange:#f08a1c;
  --red:#e2231a;
  --ink:#333333;
  --muted:#777777;
  --dark:#3a3a3a;
}
*{box-sizing:border-box;margin:0;padding:0}
html,body{width:720px;height:1200px;overflow:hidden}
body{background:var(--bg);font-family:"Noto Sans JP",sans-serif;color:var(--ink);position:relative}
.site-header{position:absolute;left:0;top:0;width:720px;height:40px;background:#fff;display:flex;align-items:center;padding:0 16px;gap:14px;border-bottom:1px solid #ccc}
.brand{display:flex;align-items:center;gap:6px;font-weight:900;font-size:19px;color:var(--blue-dark)}
.brand-dot{width:16px;height:16px;border-radius:50%;background:var(--blue)}
.tagline{font-size:7px;line-height:1.4;color:var(--muted);flex:1}
.header-contact{background:var(--dark);color:#fff;font-size:9px;padding:5px 10px;border-radius:3px}
.hero{position:absolute;left:0;top:40px;width:720px;height:212px;background:linear-gradient(#eef4f8,#d5e2ea)}
.hero-inner{position:absolute;left:67px;top:12px;width:586px;height:190px}
.hero-lead{font-size:26px;font-weight:900;color:var(--blue-dark);line-height:1.2}
.hero-lead small{display:block;font-size:20px}
.deadline{position:absolute;left:235px;top:0;width:58px;height:58px;border-radius:50%;background:var(--blue);color:#fff;font-weight:900;font-size:16px;display:flex;align-items:center;justify-content:center;line-height:1;text-align:center}
.deadline span{font-size:10px}
.hero-bar{margin-top:8px;display:inline-flex;gap:4px}
.hero-bar b{background:var(--blue);color:#fff;font-size:11px;padding:4px 7px}
.hero-price{margin-top:10px;display:flex;align-items:flex-end;gap:18px;position:relative;z-index:1}
.hero-price .now{font-size:42px;font-weight:900;color:var(--blue-dark);line-height:1;white-space:nowrap}
.hero-price .now small{font-size:14px}
.hero-price .was{font-size:12px;color:var(--ink);line-height:1.3;white-space:nowrap}
.hero-price .was strong{font-size:18px}
.device-visual{position:absolute;right:0;top:4px;width:270px;height:96px;border-radius:6px;background:linear-gradient(135deg,#b7c9d6,#6f8ea6)}
.panel{position:absolute;left:67px;width:586px;background:var(--panel);border:1px solid #c8c8c8;border-radius:6px}
.points{top:262px;height:210px}
.points-head{position:absolute;left:24px;top:20px;display:flex;align-items:center;gap:10px}
.points-badge{border:2px solid var(--blue);border-radius:14px;padding:3px 10px;font-size:11px;font-weight:700;color:var(--blue-dark);line-height:1.2;text-align:center}
.points-title{font-size:28px;font-weight:900;color:var(--ink)}
.points-title em{font-style:normal;color:var(--orange);font-size:36px}
.point-list{position:absolute;left:6px;top:82px;display:flex;gap:10px}
.point{width:130px;height:118px;border-radius:50%;background:radial-gradient(circle at 50% 35%,#5fb6ea,var(--blue));color:#fff;text-align:center;padding-top:14px}
.point .label{display:inline-block;background:#fff;color:var(--blue);font-size:10px;font-weight:700;border-radius:8px;padding:1px 8px}
.point h3{font-size:19px;font-weight:900;margin-top:6px}
.point p{font-size:8px;line-height:1.35;margin-top:4px;padding:0 12px}
.staff-photo{position:absolute;right:10px;top:-6px;width:150px;height:214px;background:linear-gradient(#f2f2f2,#cfd6dc);border-radius:4px}
.campaign{top:482px;height:300px}
.campaign-title{position:absolute;left:24px;top:14px;font-size:24px;font-weight:900;color:var(--orange)}
.campaign-title span{color:var(--ink);font-size:20px}
.plan-stack{position:absolute;left:76px;top:72px;width:194px;text-align:center}
.plan-item{background:linear-gradient(#3da6e4,var(--blue));color:#fff;font-weight:700;font-size:15px;padding:5px 0;border-radius:3px}
.plus{font-size:20px;font-weight:900;color:var(--blue-dark);line-height:1.1}
.equals{position:absolute;left:286px;top:106px;font-size:44px;font-weight:900;color:var(--blue-dark)}
.price-box{position:absolute;left:340px;top:78px;width:230px}
.price-box .was{font-size:12px}
.price-box .was strong{font-size:17px;display:block}
.price-box .arrow{display:block;margin:2px 0 0 30px}
.price-box .now-label{font-size:13px;color:var(--red);font-weight:700}
.price-box .now{font-size:40px;font-weight:900;color:var(--red);line-height:1;white-space:nowrap}
.price-box .now small{font-size:14px}
.limit-badge{position:absolute;right:14px;top:16px;width:140px;height:84px;background:var(--orange);color:#fff;border-radius:6px;text-align:center;font-weight:900;font-size:14px;line-height:1.3;padding-top:8px}
.limit-badge strong{font-size:20px}
.notes{position:absolute;left:76px;top:228px;width:490px;font-size:8px;line-height:1.5;color:var(--ink)}
.cta-row{position:absolute;left:67px;top:796px;width:586px;height:60px;display:flex;gap:10px}
.cta-free{width:132px;background:var(--orange);color:#fff;font-weight:900;font-size:14px;text-align:center;border-radius:5px;display:flex;flex-direction:column;justify-content:center;line-height:1.3}
.cta-main{flex:1;background:var(--dark);color:#fff;font-weight:700;font-size:20px;border-radius:5px;display:flex;align-items:center;justify-content:center;gap:12px}
.flow{top:868px;height:332px;border-radius:6px 6px 0 0;overflow:hidden}
.flow-title{height:82px;padding:26px 24px;font-size:26px;font-weight:700;color:var(--ink)}
.flow-title em{font-style:normal;color:var(--blue)}
.flow-body{height:250px;background:var(--blue-light);border-top:1px solid #bcd9ee}
</style>
</head>
<body>
<header class="site-header">
  <div class="brand"><span class="brand-dot"></span>karunetox</div>
  <p class="tagline">スマートフォンサイト制作／WEBサイト制作／業務システム構築<br>お客様の目線で考えたホームページ制作をお届けします。</p>
  <div class="header-contact">お問合せはこちら</div>
</header>

<section class="hero">
  <div class="hero-inner">
    <h1 class="hero-lead"><small>先着10名様</small>限定キャンペーン!!</h1>
    <div class="deadline"><div>6/28<br><span>まで</span></div></div>
    <div class="hero-bar"><b>ページ制作5ページ</b><b>問い合わせフォーム</b><b>初期費用</b></div>
    <div class="hero-price">
      <div class="now">63,000<small>円（税込み）</small></div>
      <div class="was">通常価格<br><strong>149,100</strong>円（税込）</div>
    </div>
    <div class="device-visual" role="img" aria-label="パソコンとスマートフォンに表示された制作サイトの画面例"></div>
  </div>
</section>

<section class="panel points">
  <div class="points-head">
    <div class="points-badge">karunetox<br>だから出来る</div>
    <h2 class="points-title"><em>3</em>つのポイント</h2>
  </div>
  <div class="point-list">
    <div class="point"><span class="label">Point1</span><h3>SEO対策</h3><p>SEOで上位表示を行います</p></div>
    <div class="point"><span class="label">Point2</span><h3>スマホ対応</h3><p>PC・スマートフォンに最適化されたページを提供します</p></div>
    <div class="point"><span class="label">Point3</span><h3>無料サポート</h3><p>納品後のサポート6ヶ月無料サービス付き</p></div>
  </div>
  <div class="staff-photo" role="img" aria-label="資料を手に案内するスタッフの写真"></div>
</section>

<section class="panel campaign">
  <h2 class="campaign-title">キャンペーン価格<span>のご紹介</span></h2>
  <div class="plan-stack">
    <div class="plan-item">ページ制作5ページ</div>
    <div class="plus">＋</div>
    <div class="plan-item">問い合わせフォーム</div>
    <div class="plus">＋</div>
    <div class="plan-item">初期費用</div>
  </div>
  <div class="equals">＝</div>
  <div class="price-box">
    <div class="was">通常価格<strong>149,100円（税込）</strong></div>
    <svg class="arrow" width="30" height="16" viewBox="0 0 30 16"><path d="M8 0h14v6h8L15 16 0 6h8z" fill="#f08a1c"/></svg>
    <div class="now-label">キャンペーン価格</div>
    <div class="now">63,000<small>円（税込）</small></div>
  </div>
  <div class="limit-badge">【先着10名様】<br><strong>限定!</strong><br>6/28日まで</div>
  <p class="notes">※初期費用は、ドメイン取得代行・レンタルサーバ取得代行を含みます。<br>※ページ制作は5ページまでとなります。<br>※ドメイン代＜年額:850円～＞、レンタルサーバ代＜年額4,725円～＞は別途お客様にてご負担頂きます。<br>※ホームページに掲載する画像を撮影することも可能です（但し、別途費用が発生します）</p>
</section>

<nav class="cta-row">
  <div class="cta-free">お問合せ相談<br>無料</div>
  <div class="cta-main">
    <svg width="30" height="22" viewBox="0 0 30 22"><rect x="1" y="1" width="28" height="20" fill="#fff"/><path d="M1 1l14 11L29 1" fill="none" stroke="#3a3a3a" stroke-width="2"/></svg>
    お問合せはこちら
  </div>
  <div class="cta-free">お見積り<br>無料</div>
</nav>

<section class="panel flow">
  <h2 class="flow-title">制作の<em>流れ</em></h2>
  <div class="flow-body"></div>
</section>
</body>
</html>
```